Letterhead/Envelope Design Project

We are a 501c3 non-profit that supports educational programs at Dunmoral Fern Hollow State Park in California. We have new logo and need letterhead. The design needs need incorporate the logo attached. It needs to contain the information in document attached called "information" attached. Please see our website fernhollow.org to get the feeling and colors we are looking for.

```html
<!DOCTYPE html>
<html lang="en">
<head>
<meta charset="utf-8">
<title>Fern Hollow Association – Stationery</title>
<link href="https://fonts.googleapis.com/css2?family=Arimo:wght@400;700&display=swap" rel="stylesheet">
<style>
  :root {
    --forest: #1c4d1e;
    --forest-dark: #0f3a12;
    --rule: #123d14;
    --paper: #ffffff;
    --page-bg: #ffffff;
    --tag-brown: #4a2a1c;
    --contact-green: #2f6b2a;
    --window: #d7dcdc;
    --cream: #f4f1dc;
    --shadow: rgba(0,0,0,0.28);
  }
  * { margin: 0; padding: 0; box-sizing: border-box; }
  html, body { width: 1200px; height: 1200px; overflow: hidden; background: var(--page-bg); }
  body { position: relative; font-family: "Arimo", Arial, sans-serif; }
  address { font-style: normal; }

  .letterhead {
    position: absolute; left: 100px; top: 160px; width: 682px; height: 880px;
    background: var(--paper); box-shadow: 5px 6px 8px var(--shadow);
    border: 1px solid #e4e4e4;
  }
  .letterhead__header { position: absolute; left: 0; top: 0; width: 100%; height: 78px; background: var(--forest); }
  .letterhead__rule { position: absolute; left: 0; top: 96px; width: 100%; height: 3px; background: var(--rule); }
  .letterhead__tagline {
    position: absolute; left: 135px; top: 82px; font-size: 11.5px; letter-spacing: 3px;
    color: var(--tag-brown); white-space: nowrap;
  }
  .letterhead__contact {
    position: absolute; left: 552px; top: 16px; font-size: 6.5px; line-height: 8.6px; color: #fff;
  }
  .letterhead__footer {
    position: absolute; left: 0; bottom: 0; width: 100%; height: 33px; background: var(--forest-dark);
    color: #e9efe3; font-size: 7.6px; letter-spacing: 0.6px; text-align: center; line-height: 33px;
    white-space: nowrap;
  }

  .brand-mark {
    position: absolute; background: var(--forest); display: flex; align-items: center; justify-content: center;
    text-align: center; color: #fff; font-weight: 700; line-height: 1.1;
  }
  .letterhead .brand-mark { left: 49px; top: 9px; width: 73px; height: 84px; font-size: 10px; }

  .envelope {
    position: absolute; left: 410px; top: 322px; width: 690px; height: 572px;
    background: var(--paper); box-shadow: 5px 6px 8px var(--shadow);
    border-radius: 55px 55px 0 0; border: 1px solid #e4e4e4;
  }
  .envelope__flap {
    position: absolute; left: 0; top: 0; width: 100%; height: 122px; background: var(--forest);
    border-radius: 55px 55px 0 0;
  }
  .envelope__flap-tagline {
    position: absolute; top: 56px; transform: rotate(180deg);
    color: #fff; font-size: 12px; letter-spacing: 3.4px; white-space: nowrap;
  }
  .envelope__flap-tagline--start { left: 396px; }
  .envelope__flap-tagline--end { left: 112px; }
  .envelope__flap .brand-mark {
    left: 306px; top: 17px; width: 75px; height: 89px; font-size: 10px;
    transform: rotate(180deg); background: var(--forest-dark);
  }
  .envelope__return .brand-mark { left: 45px; top: 209px; width: 72px; height: 85px; font-size: 10px; }
  .envelope__contact {
    position: absolute; left: 132px; top: 215px; font-size: 7.6px; line-height: 10.4px; color: var(--contact-green);
  }
  .envelope__band { position: absolute; left: 0; top: 369px; width: 100%; height: 92px; background: var(--forest); }
  .envelope__band-tagline {
    position: absolute; left: 23px; top: 39px; color: var(--cream); font-size: 13px; letter-spacing: 3.4px;
    white-space: nowrap;
  }
  .envelope__window {
    position: absolute; left: 342px; top: 356px; width: 299px; height: 120px;
    background: var(--window); border-radius: 24px;
  }
</style>
</head>
<body>

<section class="letterhead" aria-label="Letterhead">
  <div class="letterhead__header"></div>
  <div class="brand-mark">FERN<br>HOLLOW<br>ASSOCIATION</div>
  <address class="letterhead__contact">
    Fern Hollow Association<br>
    P.O. Box 4470<br>
    Dunmoral, CA 95999-4470<br>
    Phone: 555.014.2290<br>
    Fax: &nbsp;555.014.2291<br>
    email: fha@fernhollow.org<br>
    website: &nbsp;fernhollow.org
  </address>
  <p class="letterhead__tagline">WANDERING QUIET AMONG FERNS</p>
  <div class="letterhead__rule"></div>
  <footer class="letterhead__footer">OUR PURPOSE: TO FUND WELCOMING OUTDOOR LEARNING AND NATURE GUIDANCE FOR EVERY VISITOR TO DUNMORAL FERN HOLLOW STATE PARK</footer>
</section>

<section class="envelope" aria-label="Envelope">
  <div class="envelope__flap">
    <div class="brand-mark">FERN<br>HOLLOW<br>ASSOCIATION</div>
    <p class="envelope__flap-tagline envelope__flap-tagline--start">WANDERING QUIET</p>
    <p class="envelope__flap-tagline envelope__flap-tagline--end">AMONG FERNS</p>
  </div>
  <div class="envelope__return">
    <div class="brand-mark">FERN<br>HOLLOW<br>ASSOCIATION</div>
    <address class="envelope__contact">
      Fern Hollow Association<br>
      P.O. Box 4470<br>
      Dunmoral, CA 95999-4470<br>
      Phone: 555.014.2290<br>
      Fax: &nbsp;555.014.2291<br>
      email: fha@fernhollow.org<br>
      website: &nbsp;fernhollow.org
    </address>
  </div>
  <div class="envelope__band">
    <p class="envelope__band-tagline">WANDERING QUIET AMONG FERNS</p>
  </div>
  <div class="envelope__window" aria-label="Address window"></div>
</section>

</body>
</html>
```